quiet meadow therapy (QMT)

I need to build a website for my therapy business.
There are two parts to the website
on the landing page; they choose whether they are therapists making a referral or patients needing more information.
After that, they are taken to their respective pages.
There is the textual information and a referral form on the therapist page, and on the patient page, the text is a bit different, and there will be a booking page on the patient page.
Visually minimal, it's a therapeutic website. I want it clean, clinical, and modern
colors: greenish blue or maybe orangish
PHP/html code
Updates

Hi everyone
I'm very sorry for the lack of responses to your designs. I am trying to work it out, but this platform has been a challenge for me.
I appreciate everyone's efforts, and I am unsure how to rate designs and move forward with the ones I like. There is a 5-star rating, but I don't understand how I'm supposed to politely say that it is not it without feeling like I'm going to affect someone's future rating negatively.
Please understand me. Thank you

Designs look the same

Target Market(s)

therapy and stress management

Industry/Entity Type

stress management therapy

Coding

Coded - Design and coding required

Number of Pages Required

5+ page

Font styles to use
Serif

Colors
0094D4
00A9DD
6FCCEA
C7EBF8
E9F6FB
00AB8E
00BBA5
67D7C9
C6EFE9
E9F9F6

Requirements
Must have
• landing page that that have 2 options. one for therapist another for patient

```html
<!DOCTYPE html>
<html lang="en">
<head>
<meta charset="utf-8">
<title>QMT — Enrollment</title>
<link rel="stylesheet" href="https://fonts.googleapis.com/css2?family=Poppins:wght@400;500;600;700;800&display=swap">
<style>
:root{
  --ink:#1d1f24;
  --hero-dark:#1f2733;
  --hero-mid:#35404c;
  --band:#47748c;
  --band-line:#5d879c;
  --orange:#fbab5b;
  --teal:#19b6a0;
  --teal-soft:#7fd0c6;
  --field:#f1f1f1;
  --field-text:#6b6b6b;
  --white:#ffffff;
  --rule:#dcdcdc;
}
*{box-sizing:border-box;margin:0;padding:0}
html,body{width:907px;height:1200px;overflow:hidden}
body{font-family:"Poppins",sans-serif;color:var(--ink);position:relative;background:var(--band)}
.hero{position:absolute;left:0;top:0;width:907px;height:605px;overflow:hidden;
  background:radial-gradient(ellipse 220px 280px at 470px 280px,#4a4f57 0%,#2e3742 60%,transparent 100%),
  linear-gradient(160deg,var(--hero-mid) 0%,var(--hero-dark) 100%)}
.brand{position:absolute;left:66px;top:15px;display:flex;align-items:center;gap:8px;color:var(--white)}
.brand-dot{width:26px;height:26px;border-radius:50%;background:var(--teal)}
.brand-name{font-weight:500;font-size:24px;letter-spacing:10px;line-height:1}
.brand-sub{position:absolute;left:70px;top:56px;color:var(--white);font-size:6.3px;font-weight:600;letter-spacing:.6px}
.menu{position:absolute;left:815px;top:29px;width:26px}
.menu span{display:block;height:3px;background:var(--orange);margin-bottom:4px;margin-left:auto}
.title{position:absolute;left:66px;top:180px;color:var(--white);font-weight:800;font-size:47px;letter-spacing:-.5px}
.subtitle{position:absolute;left:66px;top:240px;color:var(--white);font-size:15px}
.card{position:absolute;background:var(--white);padding:0 27px}
.card h2{font-size:14.5px;font-weight:700;letter-spacing:.3px;padding:19px 1px 15px;border-bottom:1px solid var(--rule)}
.label{display:block;font-size:9.5px;font-weight:600;margin:18px 2px 6px}
.label sup{font-weight:400;font-size:8px;vertical-align:top}
.field{height:37px;border-radius:19px;background:var(--field);color:var(--field-text);font-size:10.5px;padding:0 24px;display:flex;align-items:center;justify-content:space-between}
.contact{left:233px;top:324px;width:294px;height:151px}
.payment{left:546px;top:106px;width:294px;height:368px}
.payment .label{margin-top:21px}
.cvv{width:28px;height:17px}
.check{display:flex;align-items:center;gap:8px;font-size:10.5px;margin:10px 3px 12px}
.check i{width:11px;height:11px;border:1px solid #9a9a9a}
.submit{height:37px;border-radius:19px;background:var(--orange);color:var(--white);font-weight:700;font-size:13px;display:flex;align-items:center;justify-content:center;position:relative}
.submit svg{position:absolute;right:16px}
.pager{position:absolute;left:851px;top:239px}
.pager span{display:block;width:12px;height:12px;border-radius:50%;margin-bottom:6px}
.pager .on{border:1.5px solid var(--teal);background:radial-gradient(circle,var(--teal) 30%,transparent 35%)}
.pager .off{width:9px;height:9px;margin-left:1.5px;background:#6c7480}
.cta{position:absolute;left:112px;top:650px;color:var(--white);font-weight:800;font-size:26.5px;letter-spacing:-.5px}
.cta-btn{position:absolute;left:632px;top:648px;width:153px;height:39px;border-radius:20px;background:var(--orange);color:var(--white);font-weight:600;font-size:9.8px;display:flex;align-items:center;justify-content:center}
.rule{position:absolute;left:67px;width:773px;height:1px;background:var(--band-line)}
.foot-brand{position:absolute;left:0;width:907px;top:835px;display:flex;justify-content:center;align-items:center;gap:20px;color:var(--white)}
.foot-dot{width:64px;height:64px;border-radius:50%;background:var(--teal-soft)}
.foot-name{font-weight:600;font-size:80px;letter-spacing:30px;line-height:1}
.foot-sub{position:absolute;left:0;width:907px;top:942px;text-align:center;color:var(--white);font-weight:600;font-size:17px;letter-spacing:1.6px}
.nav{position:absolute;left:0;width:907px;top:993px;display:flex;justify-content:center;gap:34px;color:var(--white);font-size:11.5px}
.social{position:absolute;left:380px;top:1036px;display:flex;gap:7px}
.social span{width:31px;height:31px;border-radius:50%;background:#57819a;display:flex;align-items:center;justify-content:center}
.social span i{width:9px;height:9px;border-radius:50%;background:var(--white)}
.copy{position:absolute;left:0;width:907px;top:1174px;text-align:center;font-size:10px;color:#1f2e38}
.chat{position:absolute;left:840px;top:1146px;width:41px;height:41px;border-radius:50%;background:var(--orange);display:flex;align-items:center;justify-content:center}
</style>
</head>
<body>
<section class="hero" role="img" aria-label="Photo of a paper head silhouette with torn paper ribbons unravelling from it">
</section>
<header>
  <div class="brand"><span class="brand-dot"></span><span class="brand-name">QMT</span></div>
  <div class="brand-sub">QUIET MEADOW THERAPY</div>
  <div class="menu"><span style="width:26px"></span><span style="width:20px"></span><span style="width:26px"></span></div>
</header>
<h1 class="title">ENROLLMENT</h1>
<p class="subtitle">Sign up for QMT today</p>

<div class="card contact">
  <h2>CONTACT</h2>
  <span class="label">EMAIL ADDRESS<sup>*</sup></span>
  <div class="field">Enter email address</div>
</div>

<div class="card payment">
  <h2>PAYMENT</h2>
  <span class="label">CARD INFORMATION<sup>*</sup></span>
  <div class="field">2424 5254 2445 2145</div>
  <span class="label">EXPIRATION DATE<sup>*</sup></span>
  <div class="field">8-12-2022</div>
  <span class="label">SECURITY CODE<sup>*</sup></span>
  <div class="field">Enter Code
    <svg class="cvv" viewBox="0 0 28 17"><rect x="0" y="3" width="24" height="14" rx="2" fill="#e3e6ea"/><rect x="0" y="6" width="24" height="2" fill="#c9ced5"/><circle cx="21" cy="6" r="6" fill="#3e4a5a"/><text x="21" y="8" font-size="5" fill="#fff" text-anchor="middle" font-family="Poppins,sans-serif">135</text></svg>
  </div>
  <div class="check"><i></i>Billing is same as shipping information</div>
  <div class="submit">SUBMIT
    <svg width="13" height="12" viewBox="0 0 13 12"><path d="M0 6 13 0 10 12 6 8 11 2 4 7Z" fill="#fff"/></svg>
  </div>
</div>

<div class="pager"><span class="on"></span><span class="off"></span></div>

<h2 class="cta">GOT MORE QUESTIONS ABOUT QMT?</h2>
<div class="cta-btn">CHECK OUT OUR FAQS</div>
<div class="rule" style="top:726px"></div>

<div class="foot-brand"><span class="foot-dot"></span><span class="foot-name">QMT</span></div>
<div class="foot-sub">QUIET MEADOW THERAPY</div>
<nav class="nav"><span>HOME</span><span>WHAT IS QMT?</span><span>COURSES</span><span>ENROLLMENT</span><span>MEET THE TEAM</span><span>FAQ</span></nav>
<div class="social"><span><i></i></span><span><i></i></span><span><i></i></span><span><i></i></span></div>

<div class="rule" style="top:1163px"></div>
<p class="copy">© COPYRIGHT 2022 | ALL RIGHTS RESERVED</p>
<div class="chat"><svg width="22" height="18" viewBox="0 0 22 18"><path d="M11 1C5.5 1 1 4.4 1 8.5c0 2.3 1.4 4.3 3.6 5.7L3.5 17l4.3-2c1 .3 2.1.4 3.2.4 5.5 0 10-3.3 10-7.4S16.5 1 11 1Z" fill="#fff"/><circle cx="7" cy="8.5" r="1.3" fill="#fbab5b"/><circle cx="11" cy="8.5" r="1.3" fill="#fbab5b"/><circle cx="15" cy="8.5" r="1.3" fill="#fbab5b"/></svg></div>
</body>
</html>
```